Business Card for Flight Instructor/Commercial Pilot

I need a business card for myself as a Flight Instructor. I'm a certificated flight instructor at a local flight school in St Paul, MN and want to have a business card that I can give out both to prospective students and also to prospective employers in commercial/business aviation. The business card should have a few elements to it (my name, my position, and my ZRT certifications:
Dorian Welkes, MBA
Flight Instructor
CFI, CFII, AGI, IGI
Then lastly, I'd like it to include my phone number for calls or texts, my email address, and my Corvanet url. I'll provide all of these at a later point.

If we can include some kind of aviation graphic, that's great, but I don't currently have a logo and I don't necessarily need one, so don't feel like a logo is required here, it's not. I'm but I'm open to whatever you might put together. But I honestly don't need a logo, just good design with a simple graphic element to draw a little interest.
I'd also like to add a short tag line. A few ideas I have are:
- Fly Smart. Stay Humble. Never Stop Learning.
- Train smart. Fly safe. Have fun.
- Master the craft. Enjoy the flight.

For the back side, I'm open to ideas on what to put there. maybe the tagline could go there, or a QR code for my Corvanet page, or maybe something else.

Target audience is both prospective students who are interested in learning to fly (or adding more ratings) and commercial aviation companies that could be potential employer for me in commercial aviation. Trying to portray a sense of professionalism, trust, and high level of competency.

The business card doesn’t have to be standard (rectangular with square corners) and I’m open to suggestions for based on the design.
Lastly, I just don't want the design created by AI.
Let me know if you need any further info. Thanks!

```html
<!DOCTYPE html>
<html lang="en">
<head>
<meta charset="utf-8">
<title>Dorian Welkes – Flight Instructor Business Card</title>
<link rel="stylesheet" href="https://fonts.googleapis.com/css2?family=Arimo:wght@400;700&family=Open+Sans:wght@300&display=swap">
<style>
  :root {
    --ink: #000000;
    --brown: #3a1716;
    --sky: #c9e8ea;
    --paper: #ffffff;
  }
  html, body {
    margin: 0;
    padding: 0;
    width: 1200px;
    height: 686px;
    overflow: hidden;
    background: var(--paper);
  }
  .card {
    position: relative;
    width: 1200px;
    height: 686px;
    background: var(--paper);
    overflow: hidden;
  }
  .decor {
    position: absolute;
    inset: 0;
    width: 1200px;
    height: 686px;
  }
  .decor .dark { fill: var(--brown); }
  .decor .sky { fill: var(--sky); }

  .identity {
    position: absolute;
    left: 0;
    top: 0;
    font-family: "Arimo", Arial, Helvetica, sans-serif;
    color: var(--ink);
  }
  .name {
    position: absolute;
    left: 82px;
    top: 95px;
    margin: 0;
    white-space: nowrap;
    font-weight: 700;
    font-size: 57px;
    line-height: 1;
  }
  .name .degree {
    font-weight: 400;
    font-size: 29px;
    margin-left: 6px;
  }
  .role {
    position: absolute;
    left: 86px;
    top: 173px;
    margin: 0;
    white-space: nowrap;
    font-weight: 400;
    font-size: 61px;
    line-height: 1;
  }
  .certs {
    position: absolute;
    left: 258px;
    top: 243px;
    margin: 0;
    white-space: nowrap;
    font-size: 27px;
    line-height: 1;
  }

  .contact {
    position: absolute;
    margin: 0;
    font-family: "Open Sans", Arial, sans-serif;
    font-weight: 300;
    font-size: 30px;
    line-height: 1;
    color: var(--brown);
    white-space: nowrap;
  }
  .contact.address { left: 223px; top: 378px; }
  .contact.email { left: 222px; top: 474px; }
  .contact.phone { left: 758px; top: 378px; line-height: 37px; margin-top: -7px; }
  .contact.handle { left: 770px; top: 474px; }
  .contact.web { left: 386px; top: 630px; }

  .icon {
    position: absolute;
    fill: var(--brown);
  }
  .network-label {
    position: absolute;
    left: 664px;
    top: 481px;
    display: flex;
    align-items: center;
    gap: 6px;
    font-family: "Open Sans", Arial, sans-serif;
    font-weight: 300;
    font-size: 16px;
    color: var(--brown);
  }
  .network-label .mark {
    width: 12px;
    height: 12px;
    background: var(--brown);
  }
</style>
</head>
<body>
<main class="card">
  <svg class="decor" viewBox="0 0 1200 686" aria-hidden="true">
    <path class="dark" d="M904 0 A 210 210 0 0 0 1112 118 L1200 118 L1200 0 Z"/>
    <path class="dark" d="M0 541 Q 190 542 256 686 L0 686 Z"/>
    <path class="sky" d="M0 602 Q 150 598 212 686 L0 686 Z"/>
    <path class="dark" d="M866 612 Q 866 656 880 672 L1200 672 L1200 686 L870 686 Q 862 650 866 612 Z"/>
  </svg>

  <header class="identity">
    <h1 class="name">DORIAN WELKES<span class="degree">MBA</span></h1>
    <p class="role">Flight Instructor</p>
    <p class="certs">CFI, CFII, AGI, IGI</p>
  </header>

  <svg class="icon" style="left:138px;top:368px" width="34" height="52" viewBox="0 0 34 52" aria-hidden="true">
    <path d="M17 0 C7.6 0 0 7.6 0 17 C0 29 17 52 17 52 C17 52 34 29 34 17 C34 7.6 26.4 0 17 0 Z M17 23 A6 6 0 1 1 17 11 A6 6 0 1 1 17 23 Z"/>
  </svg>
  <p class="contact address">YOUR ADRESS LINE</p>

  <svg class="icon" style="left:130px;top:474px" width="48" height="32" viewBox="0 0 48 32" aria-hidden="true">
    <path d="M0 0 H48 V32 H0 Z M5 5 V27 H43 V5 Z"/>
    <path d="M5 5 L24 19 L43 5 L43 9 L24 23 L5 9 Z"/>
    <path d="M5 27 L19 15 L21 17 L8 27 Z M43 27 L29 15 L27 17 L40 27 Z"/>
  </svg>
  <p class="contact email">JOHN.SMITH@YOURMAIL.COM</p>

  <svg class="icon" style="left:677px;top:370px" width="50" height="48" viewBox="0 0 50 48" aria-hidden="true">
    <path d="M4 2 L12 0 L20 12 L14 18 C18 26 24 32 32 35 L38 29 L50 37 L47 46 C44 48 40 48 36 46 C20 40 8 28 2 12 C0 8 1 4 4 2 Z"/>
  </svg>
  <p class="contact phone">+0 123 456 789<br>+0 987 654 321</p>

  <div class="network-label"><span class="mark"></span><span>CORVANET</span></div>
  <p class="contact handle">JOHN.SMITH</p>

  <svg class="icon" style="left:282px;top:622px" width="48" height="48" viewBox="0 0 48 48" aria-hidden="true">
    <g fill="none" stroke="#3a1716" stroke-width="5">
      <circle cx="24" cy="24" r="21"/>
      <ellipse cx="24" cy="24" rx="9" ry="21"/>
      <line x1="3" y1="17" x2="45" y2="17"/>
      <line x1="3" y1="31" x2="45" y2="31"/>
    </g>
  </svg>
  <p class="contact web">WWW.YOURCOMPANY.COM</p>
</main>
</body>
</html>
```